Stainless Steel Water Bottle Packaging

We need a design for our cylindrical water bottle packaging.

Please see attached template (500ml cola bottle template .ai file) for exact dimensions.

VORO is defined as the elemental forces of nature embodied in an object or person. The design should be eye catching and draw potential clients in. Although its a cylindrical bottle/box, the front which would face the customer when sitting on a shelf should clearly display our logo.

Industry/Entity Type

Steel

Requirements
Must have
• Designed to the specifications of the attached template (see attached)
• Our VORO Logo (see attached) and website www.vorobottle.example(in smaller font) must appear.
• Size of bottle must appear - '17 oz/500 ml'
• These should appear somewhere:
• 'INULATED DOUBLE-WALL STAINLESS STEEL WATER BOTTLE'
• 'VORO Bottles magically keeps drinks cold for up to 24hrs, hot for 12',
• 'BPA Free'
• 'For every VORO bottle purchased, a portion of proceeds will go towards charity. Each of our colour's have been assigned a specific charity. Please visit www.vorobottle.example to find out which charity you helped support!'
• The Top circle - just our Symbol (flame/drop)
• The bottom circle - 'Inc. Designed in Canada made in China' on the outer edge leaving the middle empty for the UPC code.
• Reference website for the bottle case I'm looking for:
• http://shopkorinday.example/t-flow-lagoon-pink-insulated-water-bottle
Nice to have
• illustration of our water bottle shape (see attached) appearing somewhere on the box is something i had in mind but definitely not necessary.

```html
<!DOCTYPE html>
<html lang="en">
<head>
<meta charset="utf-8">
<title>VORO – Bottle Label and Tube Packaging</title>
<link rel="stylesheet" href="https://fonts.googleapis.com/css2?family=Montserrat:wght@600&family=Oswald:wght@300;500&family=Noto+Serif:ital@1&family=Open+Sans:wght@600&display=swap">
<style>
  :root {
    --paper: #f6f6f7;
    --brand-blue: #2fa3dc;
    --teal: #3a8c78;
    --teal-deep: #2f7565;
    --rim: #2b2f31;
    --ink-light: #ffffff;
  }
  * { margin: 0; padding: 0; box-sizing: border-box; }
  html, body { width: 1111px; height: 1200px; overflow: hidden; background: var(--paper); }
  .canvas { position: relative; width: 1111px; height: 1200px; }

  .brand-header {
    position: absolute; top: 160px; left: 0; width: 100%;
    display: flex; justify-content: center; align-items: center; gap: 18px;
  }
  .brand-header .mark-dot { width: 40px; height: 40px; border-radius: 50%; background: var(--brand-blue); }
  .brand-header .wordmark {
    font-family: "Montserrat", sans-serif; font-weight: 600;
    font-size: 86px; letter-spacing: 4px; color: var(--brand-blue); line-height: 1;
  }

  .bottle-wrap {
    position: absolute; left: 325px; top: 470px; width: 182px; height: 615px;
    background: var(--teal); border-radius: 60px 60px 22px 22px;
    color: var(--ink-light); text-align: center;
  }
  .mark-circle { width: 22px; height: 22px; border-radius: 50%; background: var(--ink-light); margin: 0 auto; }
  .bottle-wrap .mark-circle { margin-top: 135px; }
  .label-name {
    font-family: "Montserrat", sans-serif; font-weight: 600;
    font-size: 24px; letter-spacing: 2px; margin-top: 28px; line-height: 1;
  }
  .label-rule { width: 120px; height: 1.5px; background: var(--ink-light); margin: 14px auto 0; }
  .tagline {
    font-family: "Noto Serif", serif; font-style: italic; font-size: 8.5px;
    line-height: 1.3; margin-top: 9px;
  }
  .spec-table {
    width: 132px; margin: 14px auto 0; border: 1.2px solid var(--ink-light);
    font-family: "Oswald", sans-serif;
  }
  .spec-title { font-weight: 500; font-size: 8.5px; line-height: 1.45; padding: 4px 2px; border-bottom: 1.2px solid var(--ink-light); }
  .spec-note { font-family: "Open Sans", sans-serif; font-weight: 600; font-size: 5.8px; padding: 5px 2px; border-bottom: 1.2px solid var(--ink-light); }
  .spec-temps { display: flex; border-bottom: 1.2px solid var(--ink-light); }
  .spec-temp { flex: 1; padding: 4px 0 3px; font-weight: 300; font-size: 8px; line-height: 1.2; }
  .spec-temp + .spec-temp { border-left: 1.2px solid var(--ink-light); }
  .spec-temp .hours { font-weight: 500; font-size: 32px; line-height: 1.05; }
  .spec-bpa { display: flex; justify-content: center; align-items: center; gap: 3px; height: 46px; }
  .spec-bpa .bpa { font-weight: 300; font-size: 30px; line-height: 1; }
  .spec-bpa .free { font-family: "Noto Serif", serif; font-size: 10px; transform: rotate(-90deg); }
  .charity-note {
    font-family: "Open Sans", sans-serif; font-weight: 600; font-size: 5.8px;
    line-height: 1.55; letter-spacing: 0.3px; width: 132px; margin: 14px auto 0;
  }

  .tube {
    position: absolute; left: 566px; top: 360px; width: 216px; height: 738px;
    background: var(--teal-deep); border-top: 6px solid var(--rim); border-bottom: 6px solid var(--rim);
    border-radius: 3px; color: var(--ink-light); text-align: center;
  }
  .tube-lid-seam { position: absolute; left: 0; top: 150px; width: 100%; height: 3px; background: var(--rim); }
  .tube .mark-circle { margin-top: 320px; width: 24px; height: 24px; }
  .tube .label-name { font-size: 26px; margin-top: 26px; }
  .tube-volume {
    position: absolute; left: 0; bottom: 58px; width: 100%;
    font-family: "Oswald", sans-serif; font-weight: 500; font-size: 8px; letter-spacing: 0.3px;
  }
</style>
</head>
<body>
<main class="canvas">
  <header class="brand-header">
    <span class="mark-dot"></span>
    <span class="wordmark">VORO</span>
  </header>

  <section class="bottle-wrap" aria-label="Bottle label">
    <div class="mark-circle"></div>
    <div class="label-name">VORO</div>
    <div class="label-rule"></div>
    <p class="tagline">the elemental forces of nature<br>embodied in an object or person</p>
    <div class="spec-table">
      <div class="spec-title">INULATED DOUBLE-WALL STAINLESS<br>STEEL WATER BOTTLE</div>
      <div class="spec-note">VORO Bottles magically keep drinks</div>
      <div class="spec-temps">
        <div class="spec-temp">COLD<div class="hours">24</div>HRS</div>
        <div class="spec-temp">HOT<div class="hours">12</div>HRS</div>
      </div>
      <div class="spec-bpa"><span class="bpa">BPA</span><span class="free">Free</span></div>
    </div>
    <p class="charity-note">For every VORO bottle purchased, a portion of proceeds will go towards charity. Each of our colour's have been assigned a specific charity. Please visit www.vorobottle.example to find out which charity you helped support.</p>
  </section>

  <section class="tube" aria-label="Tube packaging">
    <div class="tube-lid-seam"></div>
    <div class="mark-circle"></div>
    <div class="label-name">VORO</div>
    <div class="tube-volume">17 OZ/500 ML</div>
  </section>
</main>
</body>
</html>
```